Family Nature Adventure Stay - Thistlebrook Hollow

Thistlebrook Hollow is a low environmental impact children’s farm stay and nature education experience in Devon England which presents families with the opportunity to get closer to nature.

While staying at Thistlebrook Hollow, guests will be encouraged to take part in organised nature and adventure based activities such as bird and butterfly spotting, making camps, mini beast hunts, egg collecting, star gazing, pond dipping and moth nights.

Think of the stuff you wanted to do with your parents when you were nine – fishing with Dad? Making a camp with your new friends? Clay face modelling with Mum? Convey this in your site design.

We need six pages designing:

1. Home Page
2. Accommodation & Booking
3. Events & Activities
4. Location & Interactive Map
5. Meet the Residents
6. Green Credentials

Sites we like:
http://www.craftlanehub.example/
I love this site
Full screen image slider
Stylish navigation
Very simple

www.morwennacycleworks.example
Simple design
Full screen slider
Lots of graphics
The feelof summer in the image
Moving navigation bar

http://www.glintware.example/
A really cool front page
If the images shown was a slider even better.
(I'm not hot on the length of the page)

http://platterhaus.example/
Really simple design
Very stylish
Slider half page
Great Nav icons
font for contact us

www.ninefoldstudio.example
very stylish
images
the idea of the photo book
Beautiful fonts

Target Market(s)

Our target market is young families with one or more children between 6 and 14 who love the great outddors

Industry/Entity Type

Education

Requirements
Must have
• General Design
The site in general should be very nature, holiday and children based. The natural environment, quality, adventure and comfort should be at the heart of the site.
A common styling should be used for all pages.
All pages should feature our telephone number.

The styling does not have to use elements from our logo.
Each page should have a common site navigation bar.

1. Home Page
The home page should include a brief description of what we are and what we offer. A simple page is required with a large image slider and may be a couple of other images.

The home page should feature links to our social media sites (Chatterbook & Tweetline) and the following: Heritage Keepers Guild, Timberland Stewardship Board, Garnet Vale, Nearby Beaches, Verdant Enterprise Honours.

Annexe sleeps 2+2 bed
Stables sleeps 4
Cosyburrow (Yurt) sleeps 4
Mossnest (Yurt) sleeps 4

Section should include a section for each accommodation include 360° view image, images, descriptions and embedded booking calendar from (stayplanner.example) that will feature rates and availability.
The section should note that the yurts have private bathrooms with hot showers and flushing toilets.
This section should link to the correct flyout in the interactive map to show the accommodation location.

3. Location & Interactive Map
The location map should show be a zoomable map showing our location in Devon (perhaps an embedded Mapwise map).

The map should show the layout of Thistlebrook hollow and the surrounding area with flyout images on mouse-over of certain areas with textbox descriptions. This includes the location of the accommodation, amenities, animal fields, and special sites of interest. (see SitePlan.gif for our basic map).

4. Activities & Events
This page details what we are about and what is available to see and do on site, next door at the Timberland Stewardship Board and Heritage Keepers Guild sites and nearby in Devon & Cornwall.

Activities include:
Bird and butterfly spotting, making camps, mini beast hunts, hen’s egg collecting, star gazing, pond dipping, moth nights, clay modelling, slingshot range, tree climbing, candle dipping, animal husbandry, dressing up box, story-telling, cycling, trekking, make a bird-box etc.

We intend to have competitions where children can win prizes (Thistlebrook Club)
Calendar of upcoming events
Thistlebrook club and free giveaway bath duck.
Sponsor the animals.

5. Meet the residents
This page should have a cool design like a card clash page that lists the residents and their main skills and abilities. This could be a slider, gallery based or other cool interactive feature.

The family: Colin, Rosalind and our daughters Wendy & Josephine

The animals:
Cats – Misty & Daisy the farm cats
Dogs – Pip & Fudge
Goats – Annie, Alice, Annabelle & Agatha
Sheep – Sean, Flossy & Dipstick
Chickens – Including Ronnie, Muddy, Fantastic Feathers, Lenhen & Penny
Rabbit & Guinea Pig – Angus and Funky

The wildlife:
Foxes
Badgers
Deer
Jays
Jackdaws
Sparrows
Frogs
Newts
Water boatmen
The trout
Dippers
Nuthatch
Thrush
Blackbird
Moths & Butterflies

6. Green Credentials
We have tried hard to incorporate green technologies and practices into our site. This page should showcase some of the features we have used.
Central log biomass hot water boiler (hot water and heating)
Short Rotation Coppice biomass willow plantation to supply our own logs
Rainwater runoff harvesting
Solar lighting
Water usage reduction
All electricity used is from 100% renewable sources
Off grid composting toilets
Recycled brick and concrete in the car parks
Willow Spiling (River bank protection)
Woodland management and replanting
Waste reduction & recycling point
Habitat improvement programme

The designer must be able to supply all images and graphics as part of the award. Only your own work will be accepted. Not images and designs by others.
Nice to have
• Colour schemes
Eggshell blue (9ADCED), Dark Blue (1F6991) and white
(Taken from our logo)

Green & Gold
(Fern Guards in the film Vast)

```html
<!DOCTYPE html>
<html lang="en">
<head>
<meta charset="utf-8">
<title>Events &amp; Activities – Thistlebrook Hollow</title>
<link href="https://fonts.googleapis.com/css2?family=Arimo:wght@400;700&family=Kaushan+Script&display=swap" rel="stylesheet">
<style>
:root{
  --nav-top:#2a7fae;
  --nav-bottom:#1c5b80;
  --eggshell:#9adced;
  --deep:#1f3447;
  --panel:#234b68;
  --panel-edge:#2d5a7a;
  --card:rgba(8,40,48,.88);
  --band:rgba(40,120,140,.55);
  --white:#ffffff;
  --muted:#b9c6cf;
  --alert:#e0342f;
  --link:#39a9dc;
  --frame:#d9dcdc;
  --rule:rgba(255,255,255,.12);
}
*{box-sizing:border-box;margin:0;padding:0}
html,body{width:1003px;height:1200px;overflow:hidden}
body{position:relative;background:var(--deep);font-family:"Arimo",Arial,sans-serif;color:var(--white)}
a{color:inherit;text-decoration:none}

.site-nav{position:absolute;left:0;top:0;width:1003px;height:52px;background:linear-gradient(var(--nav-top),var(--nav-bottom));border-bottom:1px solid #0f3d58;z-index:5}
.site-nav a{position:absolute;top:24px;font-size:14px;font-variant:small-caps;letter-spacing:-.4px;color:var(--white)}
.site-nav a.current{color:var(--eggshell);text-decoration:underline}
.brand{position:absolute;left:455px;top:10px;width:95px;height:40px;display:flex;flex-direction:column;align-items:center;justify-content:center;gap:3px}
.brand .dot{width:10px;height:10px;border-radius:50%;background:var(--white)}
.brand span{font-size:11px;font-weight:700;color:var(--white);text-align:center;line-height:1.1}

.hero{position:absolute;left:0;top:52px;width:1003px;height:597px;background:
  radial-gradient(ellipse 60% 40% at 30% 20%,rgba(220,235,180,.55),transparent 70%),
  radial-gradient(ellipse 50% 35% at 75% 75%,rgba(110,100,170,.35),transparent 70%),
  linear-gradient(180deg,#a9c27e 0%,#6f9443 30%,#4a7a2e 62%,#2e5a24 100%)}
.page-title{position:absolute;left:0;top:35px;width:482px;height:40px;background:var(--band);font-size:26px;font-weight:400;letter-spacing:-.8px;line-height:40px;text-align:right;padding-right:25px}
.event-name{position:absolute;left:292px;top:323px;width:330px;text-align:center;font-family:"Kaushan Script",cursive;font-size:36px;color:var(--white);letter-spacing:1.5px;white-space:nowrap}

.score{position:absolute;width:158px;height:147px;background:var(--card);padding:12px 11px 0 12px;font-size:12px;line-height:19px}
.score dl{display:grid;grid-template-columns:1fr auto}
.score dt,.score dd{margin:0}
.score .hot{color:var(--alert)}
.score .eggs{display:flex;justify-content:center;gap:3px;margin-top:11px}
.score .eggs i{width:8px;height:12px;border-radius:50%/60% 60% 40% 40%;background:var(--white)}

.more{position:absolute;left:61px;top:649px;width:879px;height:227px;background:var(--panel)}
.more h2{position:absolute;left:296px;top:-5px;width:306px;height:31px;background:var(--panel-edge);border-radius:6px;font-weight:400;font-size:19px;line-height:31px;text-align:center}
.arrow{position:absolute;top:704px;width:44px;height:107px;background:var(--panel-edge);display:flex;align-items:center;justify-content:center}
.activity{position:absolute;top:694px;width:162px;text-align:center}
.activity .thumb{width:162px;height:127px;border:6px solid var(--frame)}
.activity p{font-size:24px;letter-spacing:-.9px;margin:1px -30px 0;white-space:nowrap}

.contact{position:absolute;left:81px;top:944px;font-size:11px;color:var(--muted);letter-spacing:-.4px}
.contact a{color:var(--link)}
.signup{position:absolute;left:84px;top:976px;width:158px;height:21px;background:var(--white);color:#888;font-size:12px;padding:3px 8px;border:1px solid #999}
.signup-label{position:absolute;left:93px;top:1004px;font-size:12px;letter-spacing:-.4px}
.upcoming{position:absolute;left:536px;top:939px;color:var(--muted)}
.upcoming h3{font-weight:400;font-size:17px;letter-spacing:-.5px}
.upcoming .item{position:absolute;top:25px;width:170px;font-size:12px;line-height:19px;letter-spacing:-.3px}
.rule{position:absolute;left:74px;width:860px;height:1px;background:var(--rule)}
.partner{position:absolute;top:1044px;height:56px;background:rgba(255,255,255,.16)}
.foot-brand{position:absolute;left:462px;top:1122px;width:82px;height:40px;display:flex;flex-direction:column;align-items:center;justify-content:center;gap:3px}
.foot-brand .dot{width:9px;height:9px;border-radius:50%;background:var(--muted)}
.foot-brand span{font-size:10px;font-weight:700;color:var(--muted);text-align:center;line-height:1.1}
.foot-links{position:absolute;top:1177px;left:343px;font-size:12px;letter-spacing:-.4px;color:var(--muted)}
.foot-links a{position:absolute;white-space:nowrap}
.copyright{position:absolute;left:830px;top:1177px;font-size:12px;letter-spacing:-.3px;color:var(--muted)}
</style>
</head>
<body>

<nav class="site-nav">
  <a href="#" style="left:96px">Home</a>
  <a href="#" style="left:160px">Accomodation &amp; Booking</a>
  <a href="#" class="current" style="left:335px">Events &amp; Activities</a>
  <a href="#" style="left:560px">Location &amp; Interactive map</a>
  <a href="#" style="left:728px">Meet the residents</a>
  <a href="#" style="left:853px">Green Credentials</a>
  <div class="brand"><i class="dot"></i><span>Thistlebrook Hollow</span></div>
</nav>

<section class="hero" role="img" aria-label="Bluebell woodland with children collecting hen's eggs in baskets">
  <h1 class="page-title">EVENTS &amp; ACTIVITIES</h1>
  <p class="event-name">Hen's Egg Collecting</p>

  <article class="score" style="left:89px;top:84px">
    <p>Marriane (The Princess)</p>
    <dl><dt class="hot">Current Position:</dt><dd class="hot">6th</dd><dt>Egg Collected:</dt><dd>3</dd><dt class="hot">Egg broke:</dt><dd class="hot">1</dd><dt>Egg total:</dt><dd>4</dd></dl>
    <div class="eggs"><i></i><i></i><i></i><i></i></div>
  </article>
  <article class="score" style="left:519px;top:134px;width:153px">
    <p>Nikki &amp; Erika (The Duo)</p>
    <dl><dt class="hot">Current Position:</dt><dd class="hot">4rth</dd><dt>Egg Collected:</dt><dd>8</dd><dt class="hot">Egg broke:</dt><dd class="hot">2</dd><dt>Egg total:</dt><dd>10</dd></dl>
    <div class="eggs"><i></i><i></i><i></i><i></i></div>
  </article>
  <article class="score" style="left:802px;top:218px">
    <p>Mike (The Rising star)</p>
    <dl><dt class="hot">Current Position:</dt><dd class="hot">2nd</dd><dt>Egg Collected:</dt><dd>10</dd><dt class="hot">Egg broke:</dt><dd class="hot">3</dd><dt>Egg total:</dt><dd>13</dd></dl>
    <div class="eggs"><i></i><i></i><i></i><i></i></div>
  </article>
  <article class="score" style="left:288px;top:401px">
    <p>Dave (The King)</p>
    <dl><dt class="hot">Current Position:</dt><dd class="hot">1st</dd><dt>Egg Collected:</dt><dd>15</dd><dt class="hot">Egg broke:</dt><dd class="hot">0</dd><dt>Egg total:</dt><dd>15</dd></dl>
    <div class="eggs"><i></i><i></i><i></i><i></i></div>
  </article>
  <article class="score" style="left:686px;top:445px">
    <p>James (The Funny guy)</p>
    <dl><dt class="hot">Current Position:</dt><dd class="hot">3rd</dd><dt>Egg Collected:</dt><dd>10</dd><dt class="hot">Egg broke:</dt><dd class="hot">5</dd><dt>Egg total:</dt><dd>15</dd></dl>
    <div class="eggs"><i></i><i></i><i></i><i></i></div>
  </article>
</section>

<section class="more"><h2>More exciting things to do like...</h2></section>
<a href="#" class="arrow" style="left:44px" aria-label="Previous">
  <svg width="14" height="40" viewBox="0 0 14 40"><path d="M11 2 L3 20 L11 38" fill="none" stroke="#8fa9bb" stroke-width="3"/></svg>
</a>
<a href="#" class="arrow" style="left:917px" aria-label="Next">
  <svg width="14" height="40" viewBox="0 0 14 40"><path d="M3 2 L11 20 L3 38" fill="none" stroke="#8fa9bb" stroke-width="3"/></svg>
</a>

<figure class="activity" style="left:134px"><div class="thumb" role="img" aria-label="Silhouettes at a telescope under a sunset sky" style="background:radial-gradient(ellipse 70% 30% at 50% 100%,#f08a3a,transparent 80%),linear-gradient(#18265e,#3c3486 55%,#8a4a7a 85%,#e07a3a)"></div><p>Stargazing</p></figure>
<figure class="activity" style="left:324px"><div class="thumb" role="img" aria-label="Family trekking on a mountain trail" style="background:radial-gradient(ellipse 60% 30% at 60% 35%,#e8eef2,transparent 75%),linear-gradient(#bcd3e6,#9fb0a8 45%,#86a65a 70%,#5f8a3a)"></div><p>Trekking</p></figure>
<figure class="activity" style="left:515px"><div class="thumb" role="img" aria-label="Father and son fishing by a lake" style="background:radial-gradient(ellipse 45% 50% at 65% 55%,#e0d8c8,transparent 75%),linear-gradient(#8fb86a,#b8c4a8 55%,#9bb0b8 75%,#6e8f4e)"></div><p>Fishing</p></figure>
<figure class="activity" style="left:706px"><div class="thumb" role="img" aria-label="Children searching for mini beasts in the grass" style="background:radial-gradient(ellipse 50% 45% at 45% 70%,#d8b878,transparent 75%),linear-gradient(#4e6e32,#7a7a48 50%,#3f5e2a)"></div><p>Mini Beast Hunts</p></figure>

<p class="contact">Get in touch with us at +(12)-345-678-901 or follow us at <a href="#">Tweetline</a> or <a href="#">Chatterbook</a></p>
<div class="signup">name@email.com</div>
<p class="signup-label">Subscribe to our newsletter</p>

<section class="upcoming">
  <h3>Upcoming Events</h3>
  <p class="item" style="left:4px">7/22/13<br>- Stargazing and Moth nights</p>
  <p class="item" style="left:177px">7/25/13<br>- Fishing and Camping</p>
</section>

<div class="rule" style="top:1030px"></div>
<div class="partner" style="left:240px;width:80px" aria-label="Heritage Keepers Guild"></div>
<div class="partner" style="left:340px;width:36px" aria-label="Garnet Vale"></div>
<div class="partner" style="left:410px;top:1058px;height:30px;width:168px" aria-label="Timberland Stewardship Board"></div>
<div class="partner" style="left:598px;top:1060px;height:26px;width:90px" aria-label="Nearby Beaches"></div>
<div class="partner" style="left:710px;width:52px" aria-label="Verdant Enterprise Honours"></div>
<div class="rule" style="top:1109px;left:240px;width:540px"></div>

<div class="foot-brand"><i class="dot"></i><span>Thistlebrook Hollow</span></div>
<nav class="foot-links">
  <a href="#" style="left:0">Sitemap</a>
  <a href="#" style="left:64px">Accessibility</a>
  <a href="#" style="left:146px">Legal</a>
  <a href="#" style="left:197px">Privacy Policy</a>
  <a href="#" style="left:290px">Contact us</a>
</nav>
<p class="copyright">© Thistlebrook Hollow 2013</p>

</body>
</html>
```